I need a Facebook, Instagram post, for Outdoor Training
I need my logo,
Business name : Valmora Soccer Academy
Boys and girls Outdoor Soccer training
Passing, Kicking Shooting, Dribbling, Ball Control
Field: Brookvale Turf #5(1746 Hollowmere Lane Dunstead, MD 20419)
Time: 5:30pm-6:30pm 5-8 years old
6;30pm-7:30pm 9-12 years old
7:30pm-8:30pm 13-18 years old
Registration $210 ( Includes 1st month, registration, practice uniform)

Register online:
www.valmoraacademy.example
Phone:(240)555-0187

Target Market(s)

YOUTH KIDS

Colors
0054AA
0677BA
7BADD7
CADEEF
E8F1F8

Requirements
Must have
• blue , or black and white

```html
<!DOCTYPE html>
<html lang="en">
<head>
<meta charset="utf-8">
<title>Valmora Soccer Academy – Outdoor Training</title>
<link rel="stylesheet" href="https://fonts.googleapis.com/css2?family=Barlow+Condensed:ital,wght@0,600;0,700;0,800;1,800;1,900&family=Roboto:ital,wght@0,700;0,900;1,900&display=swap">
<style>
  :root {
    --brand-blue: #0c5aa3;
    --mid-blue: #0677ba;
    --soft-blue: #7badd7;
    --pale-blue: #cadeef;
    --card-bg: #e8ebef;
    --ink: #0a0a0a;
    --white: #ffffff;
  }
  * { margin: 0; padding: 0; box-sizing: border-box; }
  html, body { width: 1200px; height: 1200px; overflow: hidden; }
  body { background: var(--card-bg); font-family: "Roboto", Arial, sans-serif; }
  .post { position: relative; width: 1200px; height: 1200px; overflow: hidden; background: var(--card-bg); }
  .shapes { position: absolute; inset: 0; }

  .title {
    position: absolute; left: 72px; top: 62px;
    font-family: "Barlow Condensed", "Arial Narrow", sans-serif;
    font-style: italic; font-weight: 900; font-size: 158px; line-height: 156px;
    color: var(--brand-blue); letter-spacing: 1px; text-transform: uppercase;
  }

  .audience-band {
    position: absolute; left: 0; top: 400px; width: 506px; height: 129px;
    background: var(--ink); color: var(--white);
    font-family: "Barlow Condensed", "Arial Narrow", sans-serif; font-weight: 700;
    font-size: 38px; line-height: 52px; padding: 12px 0 0 76px;
  }

  .skills { position: absolute; left: 76px; top: 556px; list-style: none; }
  .skills li {
    display: flex; align-items: center; gap: 14px; height: 58px;
    font-weight: 700; font-size: 43px; color: var(--brand-blue);
  }
  .skills svg { width: 40px; height: 40px; flex: none; }

  .academy-name {
    position: absolute; left: 480px; top: 420px; width: 340px; text-align: center;
    font-family: "Barlow Condensed", "Arial Narrow", sans-serif; font-weight: 800;
    font-size: 44px; line-height: 46px; color: var(--brand-blue); text-transform: uppercase;
  }
  .academy-name .mark {
    display: block; width: 74px; height: 74px; border-radius: 50%;
    background: var(--brand-blue); margin: 0 auto 18px;
  }

  .register-box {
    position: absolute; left: 0; top: 830px; width: 509px; height: 148px;
    background: var(--ink); color: var(--white); border-top-right-radius: 34px;
    padding: 10px 0 0 76px;
  }
  .register-box .label {
    font-family: "Barlow Condensed", "Arial Narrow", sans-serif; font-weight: 700;
    font-size: 34px; line-height: 40px; text-transform: uppercase;
  }
  .contact-line { display: flex; align-items: center; gap: 8px; font-weight: 700; }
  .contact-line svg { width: 28px; height: 28px; flex: none; }
  .contact-line.phone { font-size: 38px; line-height: 48px; }
  .contact-line.web { font-size: 25px; line-height: 36px; }

  .registration {
    position: absolute; left: 616px; top: 732px; color: var(--white);
  }
  .registration .label { font-family: "Barlow Condensed", sans-serif; font-weight: 700; font-size: 27px; }
  .registration .price {
    font-family: "Barlow Condensed", sans-serif; font-weight: 800; font-size: 92px; line-height: 84px;
    text-shadow: 2px 3px 4px rgba(0,0,0,.35);
  }
  .registration .includes {
    font-family: "Barlow Condensed", sans-serif; font-style: italic; font-weight: 800;
    font-size: 22px; margin-top: 6px;
  }

  .venue {
    position: absolute; left: 76px; top: 1010px; color: var(--brand-blue);
    font-family: "Barlow Condensed", "Arial Narrow", sans-serif; font-weight: 700;
  }
  .venue .field { font-size: 46px; line-height: 54px; }
  .venue .address { font-size: 35px; line-height: 47px; }

  .schedule {
    position: absolute; left: 612px; top: 1004px; color: var(--ink);
    font-style: italic; font-weight: 900; font-size: 27px;
  }
  .schedule .heading { line-height: 38px; }
  .schedule table { border-collapse: collapse; }
  .schedule td { padding: 0; height: 40px; }
  .schedule td.slot { width: 285px; }
</style>
</head>
<body>
<main class="post">
  <svg class="shapes" width="1200" height="1200" viewBox="0 0 1200 1200">
    <defs>
      <linearGradient id="photoTone" x1="0" y1="0" x2="0.3" y2="1">
        <stop offset="0" stop-color="#e9d9c8"/>
        <stop offset="0.45" stop-color="#c9a97a"/>
        <stop offset="0.75" stop-color="#c8b23a"/>
        <stop offset="1" stop-color="#8fb0c4"/>
      </linearGradient>
    </defs>
    <path class="soft-curve" d="M0 1200 L0 1050 C60 1030 160 1060 220 1110 C260 1150 300 1180 340 1200 Z" fill="var(--pale-blue)" opacity="0.7"/>
    <g role="img" aria-label="Photo of a player's foot resting on a yellow soccer ball">
      <path d="M1200 170 L1200 880 L820 880 C820 760 830 640 900 560 C950 500 980 420 1040 360 C1090 310 1150 280 1200 170 Z" fill="url(#photoTone)"/>
    </g>
    <path class="accent-curve" d="M825 432 C900 430 940 360 980 300 C1020 240 1060 210 1110 200" fill="none" stroke="var(--brand-blue)" stroke-width="10" stroke-linecap="round"/>
    <circle class="accent-dot" cx="791" cy="329" r="14" fill="var(--brand-blue)"/>
    <path class="price-blob" d="M556 870 C556 760 640 720 740 728 C860 738 960 770 1040 720 C1100 680 1150 640 1200 660 L1200 880 C1130 880 1080 950 990 985 C900 1012 660 1015 600 975 C570 955 556 910 556 870 Z" fill="var(--brand-blue)"/>
  </svg>

  <h1 class="title">Valmora Soccer<br>Academy</h1>

  <div class="audience-band">Boys and girls Outdoor<br>Soccer training</div>

  <ul class="skills">
    <li><svg viewBox="0 0 40 40"><circle cx="20" cy="20" r="16" fill="none" stroke="var(--brand-blue)" stroke-width="3.5"/><path d="M11 20 L18 27 L34 9" fill="none" stroke="var(--brand-blue)" stroke-width="4" stroke-linecap="round" stroke-linejoin="round"/></svg>Passing</li>
    <li><svg viewBox="0 0 40 40"><circle cx="20" cy="20" r="16" fill="none" stroke="var(--brand-blue)" stroke-width="3.5"/><path d="M11 20 L18 27 L34 9" fill="none" stroke="var(--brand-blue)" stroke-width="4" stroke-linecap="round" stroke-linejoin="round"/></svg>Dribbling</li>
    <li><svg viewBox="0 0 40 40"><circle cx="20" cy="20" r="16" fill="none" stroke="var(--brand-blue)" stroke-width="3.5"/><path d="M11 20 L18 27 L34 9" fill="none" stroke="var(--brand-blue)" stroke-width="4" stroke-linecap="round" stroke-linejoin="round"/></svg>Kicking Shooting</li>
    <li><svg viewBox="0 0 40 40"><circle cx="20" cy="20" r="16" fill="none" stroke="var(--brand-blue)" stroke-width="3.5"/><path d="M11 20 L18 27 L34 9" fill="none" stroke="var(--brand-blue)" stroke-width="4" stroke-linecap="round" stroke-linejoin="round"/></svg>Ball Control</li>
  </ul>

  <div class="academy-name"><span class="mark"></span>Valmora<br>Soccer<br>Academy</div>

  <div class="register-box">
    <p class="label">Register online:</p>
    <p class="contact-line phone"><svg viewBox="0 0 28 28"><path d="M7 4 L11 4 L13 10 L10 12 C11.5 15.5 13 17 16 18 L18 15 L24 17 L24 21 C24 23 22 24 20 24 C11 23 5 17 4 8 C4 6 5 4 7 4 Z" fill="none" stroke="var(--white)" stroke-width="2" stroke-linejoin="round"/></svg>(240)555-0187</p>
    <p class="contact-line web"><svg viewBox="0 0 28 28"><g fill="none" stroke="var(--white)" stroke-width="2"><circle cx="14" cy="14" r="11"/><ellipse cx="14" cy="14" rx="5" ry="11"/><path d="M3 14 H25 M5 8 H23 M5 20 H23"/></g></svg>www.valmoraacademy.example</p>
  </div>

  <div class="registration">
    <p class="label">Registration</p>
    <p class="price">$210</p>
    <p class="includes">(Includes 1st month, registration, practice uniform)</p>
  </div>

  <div class="venue">
    <p class="field">Field: Brookvale Turf #5</p>
    <p class="address">(1746 Hollowmere Lane<br>Dunstead, MD 20419)</p>
  </div>

  <div class="schedule">
    <p class="heading">Time:</p>
    <table>
      <tr><td class="slot">5:30pm - 6:30pm</td><td>5 - 8 years old</td></tr>
      <tr><td class="slot">6:30pm - 7:30pm</td><td>9-12 years old</td></tr>
      <tr><td class="slot">7:30pm - 8:30pm</td><td>13-18 years old</td></tr>
    </table>
  </div>
</main>
</body>
</html>
```